Business Card for beauty technology startup

Design Glowra Business Card for a Beauty, based on the website identity and colors (https://www.glowra-example.com).
Glowra is a beauty tech startup that gathers helpful product info for beauty lovers and consumers (such as availability on stores, price range and product reviews) for makeup products. The card design must be young, colorful but clean, and very modern.

Target Market(s)

woman, 15-35

Industry/Entity Type

Cosmetics

Contact Information for Business Card

Full Name, address, phone

Font styles to use
Other font styles liked:
• Advent Pro

Colors
e34297
86cfc6
ffffff
5c5c5c
e8e8e8
e667a6
b2b2b2

Requirements
Must have
• One full colored side with a creative design and another with card info
• Use Color palette: #95C5C5 and/or #D38AA5
• Use fonts: Advent Pro
• Use website identity: https://www.glowra-example.com
Nice to have
• If needed extra font: Roboto

```html
<!DOCTYPE html>
<html lang="en">
<head>
<meta charset="utf-8">
<title>Glowra Business Card</title>
<link rel="stylesheet" href="https://fonts.googleapis.com/css2?family=Open+Sans:wght@300;400;700&display=swap">
<style>
  :root {
    --teal: #7cc6c6;
    --white: #ffffff;
    --backdrop: #ecebea;
  }
  * { margin: 0; padding: 0; box-sizing: border-box; }
  html, body {
    width: 1200px;
    height: 900px;
    overflow: hidden;
    background: var(--backdrop);
    font-family: "Open Sans", Arial, sans-serif;
  }
  .stage { position: relative; width: 1200px; height: 900px; }

  .card {
    position: absolute;
    background: var(--teal);
    color: var(--white);
    overflow: hidden;
    box-shadow: 0 6px 18px rgba(0, 0, 0, 0.12);
  }

  /* Info side */
  .card-info { left: 78px; top: 34px; width: 588px; height: 364px; }
  .brand-disc {
    position: absolute;
    left: 232px;
    top: 0;
    width: 360px;
    height: 360px;
    margin-top: -1px;
    border-radius: 50%;
    background: var(--white);
    display: flex;
    align-items: center;
    justify-content: center;
  }
  .brand-disc .brand-name {
    color: var(--teal);
    font-weight: 400;
    font-size: 58px;
    letter-spacing: 2px;
  }
  .person { position: absolute; left: 31px; top: 42px; }
  .person-name { font-size: 19px; font-weight: 700; line-height: 24px; }
  .person-role { font-size: 15px; font-weight: 400; line-height: 18px; }
  .contact-list {
    position: absolute;
    left: 31px;
    top: 204px;
    list-style: none;
    font-size: 14.5px;
    line-height: 21.5px;
  }
  .contact-list li { display: flex; align-items: center; gap: 8px; }
  .contact-list svg { width: 12px; height: 12px; fill: var(--white); flex: none; }
  .address {
    position: absolute;
    left: 31px;
    top: 285px;
    font-size: 14.5px;
    line-height: 23px;
    font-style: normal;
  }

  /* Brand side */
  .card-brand { left: 388px; top: 505px; width: 567px; height: 352px; }
  .brand-lockup {
    position: absolute;
    left: 92px;
    top: 122px;
    display: flex;
    align-items: center;
    gap: 30px;
  }
  .brand-ring {
    width: 90px;
    height: 90px;
    border: 2px solid var(--white);
    border-radius: 50%;
  }
  .brand-lockup .brand-name {
    font-size: 46px;
    font-weight: 300;
    letter-spacing: 7px;
    text-transform: uppercase;
  }
  .brand-url {
    position: absolute;
    left: 0;
    right: 0;
    top: 288px;
    text-align: center;
    font-size: 16px;
    letter-spacing: 0.5px;
  }
</style>
</head>
<body>
<main class="stage">

  <section class="card card-info" aria-label="Business card, contact side">
    <div class="brand-disc"><span class="brand-name">Glowra</span></div>

    <div class="person">
      <p class="person-name">DANIEL HARPER</p>
      <p class="person-role">Managing Director</p>
    </div>

    <ul class="contact-list">
      <li>
        <svg viewBox="0 0 24 24" aria-hidden="true"><path d="M6.6 10.8a15.1 15.1 0 0 0 6.6 6.6l2.2-2.2a1 1 0 0 1 1-.25 11.4 11.4 0 0 0 3.6.57 1 1 0 0 1 1 1V20a1 1 0 0 1-1 1A17 17 0 0 1 3 4a1 1 0 0 1 1-1h3.5a1 1 0 0 1 1 1c0 1.25.2 2.45.57 3.570a1 1 0 0 1-.25 1z"/></svg>
        (044)987650321
      </li>
      <li>
        <svg viewBox="0 0 24 24" aria-hidden="true"><rect x="2" y="5" width="20" height="14"/><path d="M3.5 6.5 12 13l8.5-6.5" fill="none" stroke="#7cc6c6" stroke-width="1.6"/></svg>
        hi@glowra-mail.com
      </li>
      <li>
        <svg viewBox="0 0 24 24" aria-hidden="true"><circle cx="12" cy="12" r="10"/><path d="M12 2c3 3 3 17 0 20M2 12h20" fill="none" stroke="#7cc6c6" stroke-width="1.6"/></svg>
        www.glowra-example.com
      </li>
    </ul>

    <address class="address">
      58, Larkspur Lane,<br>
      Brightmoor, 40512
    </address>
  </section>

  <section class="card card-brand" aria-label="Business card, brand side">
    <div class="brand-lockup">
      <span class="brand-ring" aria-hidden="true"></span>
      <span class="brand-name">Glowra</span>
    </div>
    <p class="brand-url">www.glowra-example.com</p>
  </section>

</main>
</body>
</html>
```